“Good Dog” fun and creative design sought for photo frame!

Seeking 8x10 inch photo frame with opening for dog’s photo. Dimensions must fit exact measurement specs of sample layout templates. Choose any of the three layout templates (labeled "Template 1," "Template 2" and "Template 3"). Our customers will upload their own dog’s photo to the frame and be able to print them out at 8 inches by 10 inches. The location of the opening for the dog’s photo must match one of the templates precisely. The opening for the dog's photo must have the EXACT same measurements as the templates - it cannot be round or any other shape - it must match the templates exactly. Samples of other Pawsome Snap Borders are posted just to give you a general idea of what some other designs look like from other designers. The text on the frame for this job should say “Good Dog.” Feel free to use the paw print PSD, but not required. Of course, no copyrighted materials should be used in the design.
Target Market(s)
Dog lovers
Seeking

```html
<!DOCTYPE html>
<html lang="en">
<head>
<meta charset="utf-8">
<title>Good Dog Photo Frame</title>
<link href="https://fonts.googleapis.com/css2?family=Cinzel:wght@500&display=swap" rel="stylesheet">
<style>
  :root {
    --page-bg: #e6e6e6;
    --sun-yellow: #f7ec2a;
    --mid-yellow: #f2f1a0;
    --mid-green: #cfd89a;
    --soft-white: #f4f7fb;
    --sky-blue: #a9bfe6;
    --deep-blue: #6f8fcf;
    --photo-teal: #0e5a76;
    --photo-deep: #0a3f55;
    --photo-green: #1c6a3d;
    --frame-line: #cfe3ea;
    --gold-light: #fff6dc;
    --gold-mid: #e2c98f;
    --gold-dark: #8a6a34;
    --gold-edge: #6b5127;
  }
  html, body {
    margin: 0;
    padding: 0;
    width: 1200px;
    height: 1200px;
    overflow: hidden;
    background: var(--page-bg);
  }
  .canvas {
    display: block;
    width: 1200px;
    height: 1200px;
  }
  .frame-title {
    font-family: "Cinzel", "Times New Roman", serif;
    font-weight: 500;
    text-anchor: middle;
    fill: url(#gold);
    stroke: var(--gold-edge);
    stroke-width: 1.5;
    paint-order: stroke;
  }
  .frame-title-shadow {
    font-family: "Cinzel", "Times New Roman", serif;
    font-weight: 500;
    text-anchor: middle;
    fill: var(--gold-dark);
    opacity: 0.55;
  }
  .inner-rule {
    fill: none;
    stroke: var(--frame-line);
    stroke-width: 1.5;
  }
</style>
</head>
<body>
<svg class="canvas" viewBox="0 0 1200 1200" xmlns="http://www.w3.org/2000/svg">
  <defs>
    <linearGradient id="backdrop" x1="0" y1="0" x2="0" y2="1">
      <stop offset="0" stop-color="var(--sun-yellow)"/>
      <stop offset="0.3" stop-color="var(--mid-yellow)"/>
      <stop offset="0.5" stop-color="var(--mid-green)"/>
      <stop offset="0.72" stop-color="var(--soft-white)"/>
      <stop offset="0.85" stop-color="var(--sky-blue)"/>
      <stop offset="1" stop-color="var(--deep-blue)"/>
    </linearGradient>
    <radialGradient id="glow" cx="0.5" cy="0.6" r="0.6">
      <stop offset="0" stop-color="#ffffff" stop-opacity="0.75"/>
      <stop offset="1" stop-color="#ffffff" stop-opacity="0"/>
    </radialGradient>
    <linearGradient id="photoTone" x1="0" y1="0" x2="0" y2="1">
      <stop offset="0" stop-color="var(--photo-green)"/>
      <stop offset="0.3" stop-color="var(--photo-teal)"/>
      <stop offset="1" stop-color="var(--photo-deep)"/>
    </linearGradient>
    <linearGradient id="gold" x1="0" y1="0" x2="0" y2="1">
      <stop offset="0" stop-color="var(--gold-light)"/>
      <stop offset="0.5" stop-color="var(--gold-mid)"/>
      <stop offset="0.8" stop-color="var(--gold-light)"/>
      <stop offset="1" stop-color="var(--gold-mid)"/>
    </linearGradient>
  </defs>

  <g class="photo-frame" transform="translate(130 50)">
    <rect class="frame-backdrop" width="940" height="1100" fill="url(#backdrop)"/>
    <rect class="frame-glow" width="940" height="1100" fill="url(#glow)"/>

    <text class="frame-title-shadow" x="489" y="244" font-size="178">GOOD</text>
    <text class="frame-title" x="485" y="240" font-size="178">GOOD</text>

    <g class="photo-opening" transform="translate(150 293)">
      <rect width="642" height="517" fill="url(#photoTone)" role="img" aria-label="Customer's dog photo goes here"/>
      <rect class="inner-rule" x="25" y="27" width="592" height="463"/>
      <rect class="inner-rule" x="31" y="33" width="580" height="451"/>
    </g>

    <text class="frame-title-shadow" x="472" y="1008" font-size="178">DOG</text>
    <text class="frame-title" x="468" y="1004" font-size="178">DOG</text>
  </g>
</svg>
</body>
</html>
```